Grafitti Inspired Underwear Brand Needs Website

Rex's Briefs needs a website concept for our upcoming ecommerce site. Rex’s Briefs is an underwear line targeting a male demographic between 16 and 25. The logo is in the attachments. The brand is a colorful, rebellious underwear brand targeting men who are all about getting noticed and having a good time. And especially about meeting women. We need a website concept than will transport the audience into a world of rebellion, color and fun. We are totally open to ideas, but our initial thought is its an urban, graffiti jungle. It should be a transportive web environment that will make the audience feel they are entering this other world. It could be a street setting or it could be an alleyway (googling grafitti alleyway gives some ideas) or something else.

One challenge will be to create this colorful setting against which the various navigation tabs and product pictures will stand out in such a way as to allow easy e-commerce. Maybe the setting could be a building or garage with windows that the tabs would be set against for visibility.

Here is something we really like, but we have no idea how to make the various navigation tabs visible against a background as colorful and varied as this.

http://tapestrynook.example/w/Zk7pR2m

The brand is based on colorful and edgy designs that may certainly be provocative and even sexist in some minds. Similar brands are Tornavelo and Sven Lakso (before the went unisex fitness.) Please visit those brand sites to get an idea of what the product will look like.

From an executional perspective, the primary navigation tabs are in the attached map.

Again, this is an ecommerce site so saleable product must be easily visible on the homepage and elsewhere. The basic structure should be pretty standard with Hero A’s, Hero B’s, product shots and promotion boxes all very visible, but what we need is a really cool environment concept.

Primary navigation tabs should be horizontal across the top of the site in a pretty standard fashion and are:

1. Dangerous Rex’s
2. Wild Rex’s
3. Plain Rex’s
4. All the Damn Rex’s
5. Design Rex’s
6. Rex’s Life
7. Rex’s Jokes
8. About Rex’s

Target Market(s)

Men 16-25

Number of Pages Required

1 page

Requirements
Must have
• Brand Logo.
Nice to have
• Fun use of the devil/heart logo

```html
<!DOCTYPE html>
<html lang="en">
<head>
<meta charset="utf-8">
<title>Rex's Briefs – Shop</title>
<link href="https://fonts.googleapis.com/css2?family=Oswald:wght@300;400;500;600;700&display=swap" rel="stylesheet">
<style>
:root{
  --wall-dark:#2e2a26;
  --wall-mid:#4a443d;
  --wall-light:#6a655e;
  --card-glass:rgba(200,200,200,0.32);
  --caption:#2a2a2a;
  --teal:#3fd8b4;
  --pink:#f0245a;
  --yellow:#f5c61f;
  --green:#2ec66b;
  --purple:#6a2a98;
  --footer:#1f1f1f;
  --footer-deep:#171717;
  --white:#ffffff;
  --muted:#c9c9c9;
}
*{margin:0;padding:0;box-sizing:border-box}
html,body{width:1200px;height:1200px;overflow:hidden}
body{position:relative;font-family:'Oswald',sans-serif;color:var(--white);background:var(--footer)}
.wall{position:absolute;left:0;top:0;width:1200px;height:812px;
  background:
   repeating-linear-gradient(0deg,rgba(0,0,0,.25) 0 2px,transparent 2px 26px),
   radial-gradient(ellipse at 70% 30%,var(--wall-light),transparent 60%),
   linear-gradient(180deg,var(--wall-mid),var(--wall-dark))}
.card{position:absolute;top:0;width:272px;height:397px;background:var(--card-glass);border:1px solid rgba(255,255,255,.15)}
.card-1{left:176px;border-top:3px solid var(--teal)}
.card-2{left:464px;border-top:3px solid var(--pink)}
.card-3{left:752px}
.sale-flag{position:absolute;left:0;top:0;width:100%;height:34px;background:var(--yellow);text-align:center;font-size:18px;font-weight:500;line-height:34px}
.product{position:absolute;border-radius:14px 14px 30px 30px}
.product-1{left:38px;top:100px;width:196px;height:150px;background:linear-gradient(135deg,#e0543a,#8c1d3a 60%,#e0a020)}
.product-2{left:40px;top:74px;width:192px;height:150px;background:linear-gradient(135deg,#7a2ad0,#3aa0c8 50%,#d02a6a)}
.product-3{left:40px;top:74px;width:192px;height:148px;background:linear-gradient(180deg,#b8f02a 0 16px,#222 16px)}
.sizes{position:absolute;left:12px;top:13px;display:flex;gap:11px}
.size{width:31px;height:30px;border:2px solid var(--white);border-radius:3px;font-size:14px;text-align:center;line-height:26px}
.size.out{opacity:.35}
.size.active{border-color:var(--teal);color:var(--teal)}
.add-cart{position:absolute;left:0;width:260px;top:56px;text-align:center;font-size:15px;letter-spacing:.5px;text-decoration:underline}
.caption{position:absolute;left:0;bottom:0;width:100%;height:64px;background:var(--caption);text-align:center;padding-top:9px}
.caption .name{font-size:14px;font-weight:500;line-height:18px}
.caption .price{font-size:15px;font-weight:500;margin-top:5px}
.caption s{color:var(--muted);margin-right:16px}
.arrow{position:absolute;top:188px;width:36px;height:36px;background:rgba(255,255,255,.25)}
.arrow-left{left:128px}.arrow-right{left:1036px}
.dots{position:absolute;top:437px;left:567px;display:flex;gap:11px}
.dot{width:14px;height:14px;border-radius:50%;background:var(--white)}
.dot.on{background:var(--green)}
.promo{position:absolute;left:176px;top:492px;width:560px;height:200px;overflow:hidden;
  background:linear-gradient(100deg,#c86a4a 0%,#3a3f52 35%,#1f78a8 60%,#124a78 100%)}
.promo-head{position:absolute;top:10px;width:100%;text-align:center;font-size:50px;line-height:56px;padding-right:60px}
.promo-head b{color:var(--green);font-weight:600}
.promo-head span{font-weight:300}
.promo-band{position:absolute;top:72px;width:100%;height:56px;background:var(--green);text-align:center;font-size:38px;font-weight:300;letter-spacing:2px;line-height:56px}
.shop-btn{position:absolute;left:200px;top:146px;width:160px;height:36px;background:var(--green);font-size:30px;font-weight:500;line-height:36px;text-align:center;letter-spacing:1px}
.newsletter-box{position:absolute;left:752px;top:492px;width:272px;height:200px;background:var(--purple);padding:10px}
.newsletter-box .inner{width:100%;height:100%;border:2px solid var(--white);text-align:center;padding-top:48px}
.newsletter-box .big{font-size:23px;font-weight:500;line-height:30px}
.newsletter-box hr{border:0;border-top:2px solid var(--white);width:186px;margin:12px auto 10px}
.scroll-cue{position:absolute;left:1120px;top:770px;font-size:22px;font-weight:500}
.connect{position:absolute;top:812px;left:0;width:1200px;height:306px;background:var(--footer);text-align:center}
.connect h2{font-size:40px;font-weight:600;letter-spacing:2px;margin-top:28px;line-height:48px}
.rule{width:374px;margin:8px auto 0;border-top:2px dashed var(--yellow);opacity:.8}
.connect p{font-size:18px;letter-spacing:1px;color:var(--muted);margin-top:10px}
.email{display:block;width:380px;height:31px;margin:26px auto 0;background:var(--white);color:#888;font-size:15px;line-height:31px;font-weight:300;letter-spacing:.5px;border-radius:2px}
.join{display:block;width:240px;height:56px;margin:39px auto 0;background:var(--yellow);color:#1b1b1b;font-size:42px;font-weight:600;line-height:56px;letter-spacing:2px;border-radius:3px}
.base{position:absolute;top:1118px;left:0;width:1200px;height:82px;background:var(--footer-deep);text-align:center}
.social{display:flex;justify-content:center;gap:49px;margin-top:17px}
.social i{display:block;width:26px;height:26px;border-radius:50%;background:var(--white)}
.copyright{font-size:14px;margin-top:8px}
</style>
</head>
<body>
<div class="wall" role="img" aria-label="Weathered graffiti brick wall backdrop"></div>

<article class="card card-1">
  <div class="sizes">
    <div class="size out">XS</div><div class="size">S</div><div class="size">M</div><div class="size">L</div><div class="size active">XL</div><div class="size">XXL</div>
  </div>
  <div class="add-cart">ADD TO CART</div>
  <div class="product product-1" role="img" aria-label="Product shot of colourful patterned boxer shorts"></div>
  <div class="caption"><div class="name">MEN 1-PACK SHORTS “DANCERS”</div><div class="price">32,95 USD</div></div>
</article>

<article class="card card-2">
  <div class="product product-2" role="img" aria-label="Product shot of graffiti print boxer shorts with octopus design"></div>
  <div class="caption"><div class="name">MEN 1-PACK SHORTS “OCTOREX”</div><div class="price">32,95 USD</div></div>
</article>

<article class="card card-3">
  <div class="sale-flag">ON SALE</div>
  <div class="product product-3" role="img" aria-label="Product shot of plain black boxer shorts with lime waistband"></div>
  <div class="caption"><div class="name">MEN 1-PACK SHORTS “PLAIN”</div><div class="price"><s>32,95 USD</s>26,95 USD</div></div>
</article>

<div class="arrow arrow-left"><svg width="36" height="36"><polyline points="22,9 13,18 22,27" fill="none" stroke="#fff" stroke-width="3.5"/></svg></div>
<div class="arrow arrow-right"><svg width="36" height="36"><polyline points="14,9 23,18 14,27" fill="none" stroke="#fff" stroke-width="3.5"/></svg></div>

<div class="dots"><div class="dot on"></div><div class="dot"></div><div class="dot"></div></div>

<section class="promo" role="img" aria-label="Graffiti artwork backdrop for the last day sale banner">
  <div class="promo-head"><b>LAST</b><span>DAY</span></div>
  <div class="promo-band">20% OFF “PLAIN” COLLECTION</div>
  <div class="shop-btn">SHOP NOW</div>
</section>

<aside class="newsletter-box">
  <div class="inner">
    <div class="big">GET EXTRA 15% OFF!</div>
    <hr>
    <div class="big">SIGN UP TO OUR NEWSLETTER</div>
  </div>
</aside>

<div class="scroll-cue">V</div>

<section class="connect">
  <h2>STAY CONNECTED</h2>
  <div class="rule"></div>
  <p>SUBSCRIBE TO OUR NEWSLETTER</p>
  <span class="email">type your email address here</span>
  <span class="join">JOIN US</span>
</section>

<footer class="base">
  <div class="social"><i></i><i></i><i></i></div>
  <div class="copyright">COPYRIGHT 2016 REX’S BRIEFS</div>
</footer>
</body>
</html>
```